Plox, an electronic music website !

Hi there,
We are an events agenda (festivals & parties...) specialized in all kinds of electronic music.
It's a big database where peoples come to search there next party and post comments, photos and carpoolings.
Users are between 16 and 45 years old for most of them but the majority is between 18 and 35.
They all love techno music and partying,
We are looking for a design for 2 similar pages.
PSD Uncoded design only for "homepage" and "event page".
Something cool & young but serious and clear.
Thanks

Industry/Entity Type

Events

Number of Pages Required

2 page

Font styles to use
Sans Serif

Requirements
Must have
• Homepage
• - Logo + Name (Black and White logo)
• - Banner (1428x528px in 96ppp or proportional smaller dimension)
• - Slogan "electronic events database" (find police)
• - Principal menu with : « Events », « Map », « Carpooling », « Photos » and « Infos/Contact »
• and
• - Research table (most important) with :
• « Event name », « Kind of music », « Number of people », « Date », « Continent », « Country » and an « advanced search » link.
• - A connexion zone for accounts (Sign In) and a « create account » link.
• - Some social media direct links (Lindrav, Vimzo+ and Quenlo)
• - A "focus" zone to present a special event once a month with :
• « Name », « picture (flyer) », « location », « country », « date », « kind of music », the Movara video, and a "more infos" link.
• - An "incoming" zone, with an events list (next ones, 6 or 8) :
• one line per event and, on each line :
• « Name », « picture (flyer) », « location », « country (flag) », « date » and a "more infos" link.
• - A "carpooling" zone, with the list of next carpooling (3 or 4) with on each line :
• « Event name », « picture (flyer) », « country », « date », « seats » and a « more info » link.
• - A map link picture.
• - A calendar (small and easy to understand)
• - A link to photos (only the lasts albums).
• We need a new design for this page, I put a picture of an old design I did by myself (with Paint) just to have an idea. We just want exactly the same things there is on the picture but you can move and change all elements and colors.
• This page is too long for me.
• Page 2 (Event page) : with the document « New » and « Old event page »
• Second most important page
• A lot of things on this page :
• and
• - Event name
• - Flyer (960x960px in 96ppp or proportional dimension)
• - Links to « official website », « tickets » and « add a carpooling »
• - Event informations :
• Location (Continent, Country, Adress)
• Date (from… to…)
• Kind of music
• Number of people
• Price (regular)
• Camping (yes or no)
• - Video Movara
• - Description (long text with lineup and others informations)
• - Carpoolings availables (+ an other link to add a new one)
• - Photos (+ a link to add some)
• - Others similar events (few names)
• - A « Comments » zone where users can whrite what they think about the event.
• Same thing, I made an exemple for this page, please make a new design.
• (Sorry, the website on the document is in French)
• Thanks ;)

```html
<!DOCTYPE html>
<html lang="en">
<head>
<meta charset="utf-8">
<title>Plox Events – Festivals and Parties Agents</title>
<link href="https://fonts.googleapis.com/css2?family=Open+Sans:wght@400;600;700;800&display=swap" rel="stylesheet">
<style>
:root{
  --red:#e3262e;
  --red-dark:#c81d24;
  --ink:#1d1d1d;
  --text:#555;
  --muted:#8a8a8a;
  --line:#d9d9d9;
  --field:#cfcfcf;
  --accent:#f0a22e;
  --white:#fff;
}
*{box-sizing:border-box;margin:0;padding:0}
html,body{width:1200px;height:2632px;overflow:hidden}
body{position:relative;background:var(--white);font-family:"Open Sans",Arial,sans-serif;color:var(--text)}
.abs{position:absolute}

/* header */
.brand{left:100px;top:30px;width:150px;height:135px;display:flex;flex-direction:column;align-items:center;justify-content:center;gap:8px}
.brand-mark{width:70px;height:70px;background:var(--ink)}
.brand-name{font-size:19px;font-weight:700;color:var(--ink);letter-spacing:.5px}
.tagline{left:479px;top:62px;font-size:27px;font-weight:800;color:var(--ink);letter-spacing:.2px;white-space:nowrap}
.tagline span{color:var(--red)}
.lang{left:963px;top:64px;width:139px;height:31px;border:1px solid var(--field);font-size:11px;color:var(--muted);display:flex;align-items:center;padding:0 10px;gap:8px}
.lang .flag{width:16px;height:11px;background:#8a8fa8}
.lang .caret{margin-left:auto;width:0;height:0;border:4px solid transparent;border-top-color:#888;margin-top:4px}
.main-nav{top:141px;left:540px;width:562px;display:flex;justify-content:space-between;font-size:12px;font-weight:700;color:var(--ink)}
.main-nav a{color:inherit;text-decoration:none}
.main-nav a:first-child{margin-left:10px}

/* hero */
.hero{left:0;top:188px;width:1200px;height:452px;background:radial-gradient(circle at 20% 30%,#3b6ad6 0,transparent 30%),radial-gradient(circle at 75% 25%,#e4476f 0,transparent 35%),radial-gradient(circle at 50% 70%,#c68a76 0,transparent 40%),linear-gradient(110deg,#1c2b66,#6a2a6e 45%,#c33a5d 75%,#f2a4b3)}
.search{left:153px;top:500px;width:894px;height:123px;background:var(--white);box-shadow:0 2px 10px rgba(0,0,0,.15)}
.field{position:absolute;height:32px;border:1px solid var(--field);font-size:11px;color:var(--muted);display:flex;align-items:center;padding:0 10px}
.field.select::after{content:"";margin-left:auto;border:4px solid transparent;border-top-color:#777;margin-top:4px}
.field svg{margin-left:auto}
.btn-search{position:absolute;left:450px;top:67px;width:130px;height:33px;background:var(--red);color:var(--white);font-size:11px;font-weight:700;display:flex;align-items:center;justify-content:center;gap:6px}
.adv{position:absolute;left:598px;top:76px;font-size:11px;color:var(--muted)}

/* sections */
.section-title{font-size:16px;font-weight:700;color:var(--red);text-transform:uppercase}
.rule{height:1px;background:var(--line)}
.meta{display:flex;gap:22px;font-size:11px;color:var(--muted);align-items:center;white-space:nowrap}
.meta span{display:flex;align-items:center;gap:5px}
.meta svg{width:12px;height:12px;fill:var(--accent)}

.focus-img{left:98px;top:728px;width:274px;height:193px;background:linear-gradient(135deg,#2d2420,#7a6655 50%,#1c1714)}
.focus-body{left:403px;top:728px;width:407px}
.focus-body h2{font-size:16px;font-weight:700;color:var(--red);margin-top:1px}
.focus-body .meta{margin-top:11px}
.focus-body p{margin-top:20px;font-size:11px;line-height:23.5px;color:var(--text)}
.video{left:98px;top:958px;width:712px;height:407px;background:radial-gradient(ellipse at 50% 95%,#2f56d8 0,#1a2c7a 30%,transparent 60%),linear-gradient(#3a3a3a,#1a1a1c 45%,#101330);display:flex;align-items:center;justify-content:center}
.video-badge{display:flex;align-items:center;gap:10px;color:var(--white);font-size:18px;font-weight:700}
.video-badge i{width:44px;height:44px;border-radius:50%;background:var(--red)}

.event{position:absolute;left:98px;width:712px;height:111px;border:1px solid var(--line);display:flex;padding:10px}
.event .thumb{width:124px;height:89px;flex:none}
.event .body{margin-left:22px;padding-top:16px;min-width:0}
.event h3{font-size:12.5px;font-weight:700;color:var(--red);text-transform:uppercase;white-space:nowrap}
.event p{margin-top:9px;font-size:11px;color:var(--text);white-space:nowrap}
.event .meta{margin-top:13px}

/* sidebar */
.panel{position:absolute;left:844px;width:258px;border:1px solid var(--line)}
.panel-title{font-size:11px;font-weight:700;color:var(--red);text-transform:uppercase;padding:18px 19px 0}
.create{left:844px;top:675px;width:258px;height:61px;background:var(--red);color:var(--white);display:flex;align-items:center;padding-left:22px;gap:14px}
.create strong{display:block;font-size:11px;font-weight:700}
.create small{display:block;font-size:10px}
.signin{top:752px;height:183px}
.signin-head{height:39px;background:linear-gradient(#7c7c7c,#5e5e5e);color:var(--white);font-size:11px;font-weight:700;padding:13px 19px}
.input{position:absolute;left:16px;width:223px;height:32px;border:1px solid var(--field);font-size:10px;color:var(--muted);padding:9px 12px}
.btn-red{position:absolute;background:var(--red);color:var(--white);font-weight:700;display:flex;align-items:center;justify-content:center}
.follow{top:972px;height:98px}
.follow p{position:absolute;left:19px;top:42px;width:100px;font-size:10px;line-height:17px;color:var(--text)}
.socials{position:absolute;left:135px;top:14px;display:flex;flex-direction:column;gap:6px}
.socials span{display:flex;align-items:center;gap:7px;font-size:11px;font-weight:600;color:var(--ink)}
.socials i{width:16px;height:16px;border-radius:50%;background:var(--red-dark)}
.map{top:1093px;height:237px}
.map-img{position:absolute;left:15px;top:43px;width:224px;height:177px;background:linear-gradient(140deg,#e9e5dc,#f3f0ea 40%,#dcd8cf)}
.cal-panel{top:1347px;height:214px}
.calendar{position:absolute;left:11px;top:39px;width:232px;height:163px;border:1px solid var(--line);font-size:8px;color:var(--muted)}
.cal-head{height:25px;display:flex;align-items:center;justify-content:space-between;background:#f1f1f1;font-weight:700;color:#555;font-size:8.5px}
.cal-head i{width:14px;height:25px;background:#6c8b8b;display:flex;align-items:center;justify-content:center;color:#fff;font-style:normal;font-size:9px}
.cal-grid{display:grid;grid-template-columns:repeat(7,1fr);gap:4px 6px;padding:6px 12px}
.cal-grid b{font-weight:700;color:#444;text-align:center}
.cal-grid span{height:15px;border:1px solid #e3e3e3;text-align:center;line-height:13px}
.cal-grid .off{color:#ccc}
.cal-grid .today{background:#b7ad7a;color:#fff;border-color:#b7ad7a}
.gallery{top:1598px;height:630px}
.gal{position:absolute;width:103px;height:91px}

/* footer */
.footer{left:0;top:2335px;width:1200px;height:243px;background:var(--red);color:var(--white)}
.fcol{position:absolute;top:42px}
.fcol h4{font-size:12px;font-weight:700;text-transform:uppercase;margin-bottom:8px}
.fcol li{list-style:none;font-size:11px;line-height:23px}
.fcol p{font-size:11px}
.news-input{position:absolute;left:0;top:54px;width:260px;height:32px;background:var(--white);color:var(--muted);font-size:10px;padding:9px 14px;border-radius:2px}
.subscribe{position:absolute;left:0;top:98px;width:139px;height:32px;background:#4d4d4d;color:var(--white);font-size:11px;font-weight:700;display:flex;align-items:center;justify-content:center;border-radius:2px}
.foot-brand{left:960px;top:58px;width:120px;display:flex;flex-direction:column;align-items:center;gap:6px}
.foot-brand i{width:56px;height:56px;background:var(--white)}
.foot-brand span{font-size:17px;font-weight:700}
.copyright{left:0;top:2578px;width:1200px;height:54px;background:var(--red-dark);color:var(--white);font-size:11px;display:flex;align-items:center;justify-content:center}
</style>
</head>
<body>
<svg width="0" height="0" style="position:absolute">
  <defs>
    <symbol id="ico-cal" viewBox="0 0 12 12"><rect x="1" y="2" width="10" height="9" rx="1"/><rect x="3" y="0" width="1.5" height="3"/><rect x="7.5" y="0" width="1.5" height="3"/></symbol>
    <symbol id="ico-pin" viewBox="0 0 12 12"><path d="M6 0a4 4 0 0 0-4 4c0 3 4 8 4 8s4-5 4-8a4 4 0 0 0-4-4zm0 5.5A1.5 1.5 0 1 1 6 2.5a1.5 1.5 0 0 1 0 3z"/></symbol>
    <symbol id="ico-globe" viewBox="0 0 12 12"><circle cx="6" cy="6" r="6"/></symbol>
    <symbol id="ico-seat" viewBox="0 0 12 12"><rect x="2" y="0" width="5" height="8" rx="1.5"/><rect x="2" y="7" width="9" height="3" rx="1"/><rect x="3" y="10" width="1.5" height="2"/><rect x="8.5" y="10" width="1.5" height="2"/></symbol>
  </defs>
</svg>

<header>
  <div class="abs brand"><i class="brand-mark"></i><span class="brand-name">plox.events</span></div>
  <h1 class="abs tagline">FESTIVALS AND <span>PARTIES AGENTS</span></h1>
  <div class="abs lang"><i class="flag"></i>English<i class="caret"></i></div>
  <nav class="abs main-nav"><a>EVENTS</a><a>MAP</a><a>CARPOOLING</a><a>PHOTOS</a><a>INFOS/CONTACT</a></nav>
</header>

<div class="abs hero" role="img" aria-label="Crowd of young people dancing at a party under colourful lights"></div>

<form class="abs search">
  <div class="field select" style="left:22px;top:26px;width:206px">Event name</div>
  <div class="field select" style="left:236px;top:26px;width:203px">Kind of music</div>
  <div class="field select" style="left:450px;top:26px;width:205px">Number of people</div>
  <div class="field" style="left:664px;top:26px;width:207px">Date<svg width="12" height="12" fill="#999"><use href="#ico-cal"/></svg></div>
  <div class="field select" style="left:22px;top:67px;width:206px">Continent</div>
  <div class="field select" style="left:236px;top:67px;width:203px">Country</div>
  <div class="btn-search"><svg width="11" height="11" viewBox="0 0 11 11" fill="none" stroke="#fff" stroke-width="1.8"><circle cx="4.5" cy="4.5" r="3.3"/><path d="M7 7l3 3"/></svg>SEARCH NOW</div>
  <a class="adv">Advanced Search</a>
</form>

<main>
  <h2 class="abs section-title" style="left:98px;top:667px">Focus</h2>
  <div class="abs rule" style="left:98px;top:707px;width:712px"></div>

  <div class="abs focus-img" role="img" aria-label="Flyer photo: hands playing an electric guitar"></div>
  <article class="abs focus-body">
    <h2>LOREM IPSUM IS SIMPLY DUMMY TEXT</h2>
    <div class="meta">
      <span><svg><use href="#ico-cal"/></svg>Posted on 27 March 2015</span>
      <span><svg><use href="#ico-pin"/></svg>Location</span>
      <span><svg><use href="#ico-globe"/></svg>Country</span>
    </div>
    <p>Lorem Ipsum is simply dummy text of the printing and typesetting industry. Lorem Ipsum has been the industry's standard dummy text ever since the 1500s, when an unknown printer took a galley of type and scrambled it to make a type specimen book. It has survived not only five centuries, but also the leap into electronic typesetting, remaining...</p>
  </article>

  <div class="abs video" role="img" aria-label="Event video: DJ mixing deck in front of a dancing crowd">
    <div class="video-badge"><i></i>Movara</div>
  </div>

  <h2 class="abs section-title" style="left:98px;top:1400px">Incoming Festivals</h2>
  <div class="abs rule" style="left:98px;top:1438px;width:712px"></div>

  <article class="event" style="top:1459px"><div class="thumb" role="img" aria-label="Flyer photo: turntable" style="background:linear-gradient(135deg,#cfd8e6,#44597a 60%,#1d2535)"></div><div class="body"><h3>Lorem Ipsum is simply dummy text of the printing</h3><p>Lorem Ipsum is simply dummy text of the printing and typesetting industry has been the industry's</p><div class="meta"><span><svg><use href="#ico-cal"/></svg>Posted on 27 March 2015</span><span><svg><use href="#ico-pin"/></svg>Location</span><span><svg><use href="#ico-globe"/></svg>Country</span></div></div></article>
  <article class="event" style="top:1589px"><div class="thumb" role="img" aria-label="Flyer photo: party crowd with purple lights" style="background:linear-gradient(135deg,#2a1d3d,#a2487a 55%,#3b2a5a)"></div><div class="body"><h3>Lorem Ipsum is simply dummy text of the printing</h3><p>Lorem Ipsum is simply dummy text of the printing and typesetting industry has been the industry's</p><div class="meta"><span><svg><use href="#ico-cal"/></svg>Posted on 27 March 2015</span><span><svg><use href="#ico-pin"/></svg>Location</span><span><svg><use href="#ico-globe"/></svg>Country</span></div></div></article>
  <article class="event" style="top:1717px"><div class="thumb" role="img" aria-label="Flyer photo: DJ under green lasers" style="background:linear-gradient(135deg,#0d2a10,#3fd13a 50%,#0a1f3a)"></div><div class="body"><h3>Lorem Ipsum is simply dummy text of the printing</h3><p>Lorem Ipsum is simply dummy text of the printing and typesetting industry has been the industry's</p><div class="meta"><span><svg><use href="#ico-cal"/></svg>Posted on 27 March 2015</span><span><svg><use href="#ico-pin"/></svg>Location</span><span><svg><use href="#ico-globe"/></svg>Country</span></div></div></article>

  <h2 class="abs section-title" style="left:98px;top:1854px">Next Carpoolings</h2>
  <div class="abs rule" style="left:98px;top:1891px;width:712px"></div>

  <article class="event carpool" style="top:1914px"><div class="thumb" role="img" aria-label="Event flyer: DJ in green and blue light" style="background:linear-gradient(135deg,#1f6e2d,#3ec14a 45%,#2c3f8c)"></div><div class="body"><h3>Lorem Ipsum is simply dummy text of the printing</h3><p>Lorem Ipsum is simply dummy text of the printing and typesetting industry has been the industry's</p><div class="meta"><span><svg><use href="#ico-cal"/></svg>Departure 27 March 2015</span><span><svg><use href="#ico-globe"/></svg>Country</span><span><svg><use href="#ico-seat"/></svg>3 seats left</span></div></div></article>
  <article class="event carpool" style="top:2042px"><div class="thumb" role="img" aria-label="Event flyer: turntable in pink light" style="background:linear-gradient(135deg,#7b1d8e,#e2409b 50%,#3a1660)"></div><div class="body"><h3>Lorem Ipsum is simply dummy text of the printing</h3><p>Lorem Ipsum is simply dummy text of the printing and typesetting industry has been the industry's</p><div class="meta"><span><svg><use href="#ico-cal"/></svg>Departure 27 March 2015</span><span><svg><use href="#ico-globe"/></svg>Country</span><span><svg><use href="#ico-seat"/></svg>2 seats left</span></div></div></article>
  <article class="event carpool" style="top:2171px"><div class="thumb" role="img" aria-label="Event flyer: concert crowd under orange lights" style="background:linear-gradient(135deg,#f5b33a,#c75a14 50%,#3a1a08)"></div><div class="body"><h3>Lorem Ipsum is simply dummy text of the printing</h3><p>Lorem Ipsum is simply dummy text of the printing and typesetting industry has been the industry's</p><div class="meta"><span><svg><use href="#ico-cal"/></svg>Departure 27 March 2015</span><span><svg><use href="#ico-globe"/></svg>Country</span><span><svg><use href="#ico-seat"/></svg>4 seats left</span></div></div></article>
</main>

<aside>
  <a class="abs create">
    <svg width="26" height="26" viewBox="0 0 26 26" fill="none" stroke="#fff" stroke-width="2"><rect x="2" y="6" width="17" height="17" rx="2"/><path d="M10 16l1-4 10-10 3 3-10 10z" fill="#e3262e"/></svg>
    <div><strong>CREATE AN ACCOUNT</strong><small>Click here for join us</small></div>
  </a>

  <section class="panel signin">
    <div class="signin-head">SIGN IN</div>
    <div class="input" style="top:54px">User name</div>
    <div class="input" style="top:99px">Password</div>
    <div class="btn-red" style="left:16px;top:145px;width:223px;height:37px;font-size:12px">SIGN IN</div>
  </section>

  <section class="panel follow">
    <h3 class="panel-title">Follow us</h3>
    <p>Connect with our social network</p>
    <div class="socials">
      <span><i></i>Lindrav</span>
      <span><i></i>Quenlo</span>
      <span><i></i>Vimzo+</span>
    </div>
  </section>

  <section class="panel map">
    <h3 class="panel-title">Map</h3>
    <div class="map-img" role="img" aria-label="Street map of the event area"></div>
  </section>

  <section class="panel cal-panel">
    <h3 class="panel-title" style="padding-left:15px;padding-top:15px">Calender</h3>
    <div class="calendar">
      <div class="cal-head"><i>&#8249;</i>NOVEMBER<i>&#8250;</i></div>
      <div class="cal-grid">
        <b>Mon</b><b>Tue</b><b>Wed</b><b>Thu</b><b>Fri</b><b>Sat</b><b>Sun</b>
        <span>1</span><span>2</span><span>3</span><span>4</span><span>5</span><span>6</span><span>7</span>
        <span>8</span><span>9</span><span>10</span><span>11</span><span>12</span><span>13</span><span>14</span>
        <span>15</span><span>16</span><span>17</span><span>18</span><span>19</span><span>20</span><span>21</span>
        <span>22</span><span>23</span><span>24</span><span>25</span><span>26</span><span>27</span><span>28</span>
        <span>29</span><span class="today">30</span><span>31</span><span class="off">1</span><span class="off">2</span><span class="off">3</span><span class="off">4</span>
      </div>
    </div>
  </section>

  <section class="panel gallery">
    <h3 class="panel-title">Photo gallery</h3>
    <div class="gal" style="left:16px;top:43px;background:linear-gradient(#f6c23a,#a7421d 60%,#241008)" role="img" aria-label="Gallery photo: festival crowd at sunset"></div>
    <div class="gal" style="left:136px;top:43px;background:linear-gradient(135deg,#3a3a3a,#0f0f0f)" role="img" aria-label="Gallery photo: DJ with headphones"></div>
    <div class="gal" style="left:16px;top:149px;background:linear-gradient(135deg,#c4c4c4,#2c2c2c)" role="img" aria-label="Gallery photo: headphones"></div>
    <div class="gal" style="left:136px;top:149px;background:linear-gradient(135deg,#e5eef5,#7fb3d9)" role="img" aria-label="Gallery photo: person listening to music"></div>
    <div class="gal" style="left:16px;top:255px;background:linear-gradient(135deg,#f08a1c,#5a1c06 70%)" role="img" aria-label="Gallery photo: vinyl record on fire"></div>
    <div class="gal" style="left:136px;top:255px;background:linear-gradient(135deg,#d9c9b0,#4a3a2c)" role="img" aria-label="Gallery photo: DJ wearing sunglasses"></div>
    <div class="gal" style="left:16px;top:362px;background:linear-gradient(135deg,#b37a5a,#3a2420)" role="img" aria-label="Gallery photo: fan with headphones"></div>
    <div class="gal" style="left:136px;top:362px;background:linear-gradient(135deg,#5a3a7a,#d16aa0)" role="img" aria-label="Gallery photo: singer at microphone"></div>
    <div class="gal" style="left:16px;top:469px;background:linear-gradient(135deg,#a37a52,#2b1e14)" role="img" aria-label="Gallery photo: guitarist"></div>
    <div class="gal" style="left:136px;top:469px;background:linear-gradient(#f4d23a,#d86a12 60%,#1a1006)" role="img" aria-label="Gallery photo: crowd with raised hands"></div>
    <div class="btn-red" style="left:16px;top:573px;width:223px;height:39px;font-size:12px">VIEW MORE PHOTOS</div>
  </section>
</aside>

<footer class="abs footer">
  <div class="fcol" style="left:100px"><h4>Welcome</h4><ul><li>Home</li><li>About Us</li><li>Events</li><li>Map</li><li>Carpooling</li><li>Photos</li><li>Infos/Contact</li></ul></div>
  <div class="fcol" style="left:279px"><h4>Information</h4><ul><li>Terms &amp; Conditions</li><li>Privacy Policy</li><li>Disclaimer</li><li>Sitemap</li></ul></div>
  <div class="fcol" style="left:475px"><h4>Others</h4><ul><li>My Account</li><li>Login</li><li>Register</li><li>Newsletter</li></ul></div>
  <div class="fcol" style="left:647px;width:260px"><h4>Newsletter Signup</h4><p>Get our recent updates through your email id</p>
    <div class="news-input">Enter your email id</div>
    <div class="subscribe">SUBSCRIBE</div>
  </div>
  <div class="abs foot-brand"><i></i><span>plox.events</span></div>
</footer>
<div class="abs copyright">Copyrights 2015. Plox Events. All rights reserved.</div>
</body>
</html>
```